new customer flyer 8.5 X 11 to get people who use CPAP, Snore or have sleep apnea to call us

We sell CPAP equipment and supplies in Ontario. We are designing a flyer for a an advertising campaign encouraging people to switch from the current CPAP supplier to us. Our company name is Breathwell Depot. We are different from a typical CPAP supply store in many ways. A typical store is open 9-5 monday-friday, and the customer must come to the store to get any service. We offer free delivery of supplies of the customer is using the same supplies, so they can just have their supplies shipped rather than come in to pick them up. We also offer free home visits where we will do all the services that can be done in store, including determine the best machine they need, fit them for a mask, set up their equipment and supplies, offer advice, and much more. We also offer night and weekend appointments. Finally we will buy used equipment from our customers and donate this equipment to those in the community who may not be able to afford new equipment, which has 2 benefits of reducing waste and helping the needy.

If you can come up with any other concepts to make us stand out we are open to this.

Our flyer needs to offer a call to action of providing a Prixa Gift card to new customers plus additional call to actions if you are able to create one based on info herein. The gift card amount is $50.00 if this is relevant. We can limit the number available for the promotion if you feel it would encourage a faster and quicker response rate.

The Info needed in the flyer is:
1) Company Name: Breathwell Depot
2) Phone number: 289-517-3064
3) website: www.breathwelldepot-example.com (Make creative in a way that it is easy for user to determine what it says and stimulate them to remember it.)
4) Address is optional, which is 418 Marlow Street, Fort Erie ON L2A 7K3
5) We cover the entire Niagara region and Region of Hamilton in Ontario Canada
6) A call to action is a MUST. We were thinking of using a $50 Prixa gift card for new customers or something else if you feel it would drive more calls to us or more website visits.
7) The objective is to get the customer to call us so we can make them a new customer. The secondary objective is to get the customer to visit our website, because even if they are hesitant to call us, we hope to get them to visit our website and this will give them the confidence to call us.
8) The call to action must encourage a response to hopefully get a call right away. we don't want the customer putting us on the back burner.
9) The flyer is encouraged to not only get people who have sleep apnea, snoring or are currently on CPAP to call, but to also get people who may not suffer from any of these conditions to want to give the flyer to their friends or family who does.
10) I included a bunch of pictures but they are just random pictures, you can use them, use your own or use drawings or whatever to get the message across. You do not need to use all or any of the pictures I provided.
11) We accept all health insurances

I am pretty open, so have fun with the project and be creative as possible!
Updates

There are many designs submitted but many that do not meet the requirements, and many that are similar. I am hoping to find one that does not look like every other generic design, and work with some of the designers who have submitted entries with some potential to modify them into something useable.

Target Market(s)

1) People who snore, have sleep apnea or already use CPAP.
2) Spouses of people snore or have sleep apnea, as these people notice the person who is snoring or having erratic breathing.
3) Friends or family of the people above so that they share the flyer.
4) Focus on 30-60 year old males.

Industry/Entity Type

Advertising

Colors

Designer to choose colors to be used in the design.

Requirements
Must have
• 1) Company Name: Breathwell Depot (Logo can serve as company name as well, files attached)
• 2) Phone number: 289-517-3064
• 3) website: www.breathwelldepot-example.com (Make creative in a way that it is easy for user to determine what it says and stimulate them to remember it.)
• 4) Flyer needs to be friendly and engaging.
• 5) Flyer can be funny or humorous if it will generate customers.
• 6) A call to action is a MUST. We were thinking of using a $50 Prixa gift card for new customers or something else if you feel it would drive more calls to us or more website visits.
• 7) The objective is to get the customer to call us so we can make them a new customer. The secondary objective is to get the customer to visit our website, because even if they are hesitant to call us, we hope to get them to visit our website and this will give them the confidence to call us.
• 8) The call to action must encourage a response to hopefully get a call right away. we don't want the customer putting us on the back burner.
• 9) The flyer is encouraged to not only get people who have sleep apnea, snoring or are currently on CPAP to call, but to also get people who may not suffer from any of these conditions to want to give the flyer to their friends or family who does.
• 10) I included a bunch of pictures but they are just random pictures, you can use them, use your own or use drawings or whatever to get the message across. You do not need to use all or any of the pictures I provided.
• 11) We accept all health insurances
• 12) The FLYER MUST be bold and stand out. This can be with full color, unique text or graphics, or colored backgrounds (Including really bold colors). The point is there is really not a defined market to target with this industry, so any flyers are random location flyers that must be so bold as to grab someones attention such that they want to see what the flyer says.
• 13) Because CPAP only affects about 10-15% of the population, the flyer should be designed that those who snore, suffer from sleep apnea, or CURRENTLY USE CPAP will immediately relate to the flyer and as such want to read it and hopefully call us.
Nice to have
• 1) Address is optional, which is 418 Marlow Street, Fort Erie ON L2A 7K3 (We encourage people to let us come to them, because we offer free shipping and home visits. Therefore our address is not really terribly important.
• 2) We cover the entire Niagara region and Region of Hamilton in Ontario Canada. If they get our flyer they hopefully will call us, however if this can be fit in it confirms that we service the customers area. Without it the customer may wonder if we go to the area where they live.
• 3) Our Taglines are "We make CPAP Personal" and "Better sleep for better health", if they fit into the theme of the designed flyer feel free to add one or both of these.
• 4) The flyer can be designed to appear medical in design if this works, but I prefer fun, engaging and even humorous first, and the medical part becomes secondayry.
Should not have
• 1) The flyer can not be scary or make someone feel uncomfortable.

```html
<!DOCTYPE html>
<html lang="en">
<head>
<meta charset="utf-8">
<title>Breathwell Depot – New Customer Flyer</title>
<link rel="stylesheet" href="https://fonts.googleapis.com/css2?family=Open+Sans:wdth,wght@75..100,300..800&display=swap">
<style>
  :root {
    --green: #1e9e5a;
    --green-light: #5fc287;
    --purple: #8e3f9c;
    --purple-deep: #6d2a7a;
    --ink: #3a3a3a;
    --paper: #ffffff;
    --backdrop: #d6d6d6;
    --rule: #d9d9d9;
  }
  * { box-sizing: border-box; margin: 0; padding: 0; }
  html, body { width: 1200px; height: 911px; overflow: hidden; }
  body {
    background: var(--backdrop);
    font-family: "Open Sans", Arial, sans-serif;
    position: relative;
  }
  .flyer {
    position: absolute;
    left: 270px; top: 28px;
    width: 660px; height: 854px;
    background: var(--paper);
    overflow: hidden;
    box-shadow: 0 6px 22px rgba(0,0,0,.25);
  }
  .hero-photo {
    position: absolute; left: 0; top: 0;
    width: 660px; height: 390px;
    background: linear-gradient(135deg, #e9e4dc 0%, #f4f1ec 40%, #dcd6cf 70%, #c9cfd8 100%);
  }
  .shapes { position: absolute; inset: 0; }
  .gift-badge {
    position: absolute; right: 22px; top: 22px;
    width: 230px; height: 118px;
    background: var(--purple);
    border-radius: 10px;
    color: #fff;
    padding: 10px 12px 10px 98px;
  }
  .gift-art {
    position: absolute; left: 14px; top: 22px;
    width: 74px; height: 66px;
    border-radius: 4px;
    background: linear-gradient(135deg, #2d9a4a, #e2b43a);
  }
  .gift-badge .lead { font-size: 15px; font-weight: 700; line-height: 1; }
  .gift-badge .amount { font-size: 36px; font-weight: 800; line-height: 1; }
  .gift-badge .card { font-size: 11px; font-weight: 700; text-transform: uppercase; }
  .gift-badge .who { font-size: 9px; }
  .gift-badge .cta {
    display: inline-block; margin-top: 2px;
    background: var(--green); font-size: 9px; font-weight: 800;
    padding: 1px 6px; text-transform: uppercase;
  }
  .gift-badge .limit {
    position: absolute; left: 14px; bottom: 8px;
    font-size: 7px; border: 1px solid rgba(255,255,255,.6); padding: 0 4px;
  }
  .brand {
    position: absolute; right: 30px; top: 236px;
    color: var(--green);
    font-size: 26px; font-weight: 400;
    white-space: nowrap;
  }
  .headline {
    position: absolute; left: 30px; top: 404px; width: 600px;
    font-stretch: 78%;
  }
  .headline h1 {
    color: var(--green); font-size: 40px; font-weight: 800;
    letter-spacing: .5px; line-height: 1.05; white-space: nowrap;
  }
  .headline .region {
    color: var(--purple); font-size: 27px; font-weight: 700;
    border-top: 2px solid var(--green); margin-top: 4px; padding-top: 2px;
    white-space: nowrap;
  }
  .headline .insurance { color: var(--ink); font-size: 20px; font-weight: 700; }
  .offer-pill {
    position: absolute; left: 30px; top: 528px;
    background: var(--purple); color: #fff;
    font-size: 15px; font-weight: 700;
    padding: 5px 18px; border-radius: 8px;
  }
  .benefits {
    position: absolute; left: 20px; top: 568px; width: 620px;
    display: grid; grid-template-columns: repeat(4, 1fr);
  }
  .benefit {
    text-align: center; padding: 2px 6px;
    border-left: 1px solid var(--rule);
  }
  .benefit:first-child { border-left: none; }
  .benefit-icon {
    width: 68px; height: 68px; margin: 0 auto 6px;
    border-radius: 50%;
    background: radial-gradient(circle at 40% 35%, var(--green-light), var(--green));
    border: 3px solid #cfeedd;
    display: flex; align-items: center; justify-content: center;
  }
  .benefit .free { color: var(--green); font-size: 18px; font-weight: 800; line-height: 1.1; }
  .benefit .label { color: var(--purple); font-size: 13px; font-weight: 600; line-height: 1.25; }
  .actions {
    position: absolute; left: 30px; top: 688px; width: 600px;
    display: flex; gap: 20px;
  }
  .action {
    flex: 1; border-radius: 12px; color: #fff;
    padding: 7px 16px; box-shadow: 0 4px 8px rgba(0,0,0,.2);
  }
  .action.call { background: linear-gradient(#a45bb1, var(--purple-deep)); }
  .action.web { background: linear-gradient(var(--green-light), var(--green)); }
  .action small { display: block; font-size: 13px; font-weight: 600; border-bottom: 1px solid rgba(255,255,255,.5); padding-bottom: 2px; }
  .action .big { font-size: 24px; font-weight: 800; font-stretch: 80%; white-space: nowrap; }
  .action.web .big { font-size: 16px; padding-top: 6px; }
  .action.web .hl { color: var(--purple-deep); }
  .tagline {
    position: absolute; right: 36px; bottom: 10px;
    color: #fff; font-size: 28px; font-weight: 300;
    white-space: nowrap;
  }
  .tagline b { font-weight: 700; }
</style>
</head>
<body>
  <main class="flyer">
    <div class="hero-photo" role="img" aria-label="Smiling couple relaxing in bed, the man wearing a CPAP nasal mask"></div>

    <svg class="shapes" width="660" height="854" viewBox="0 0 660 854" aria-hidden="true">
      <path d="M0,372 C180,366 280,260 360,180 C440,110 560,92 660,88 L660,854 L0,854 Z" fill="#fff"/>
      <path d="M0,372 C180,366 280,260 360,180 C440,110 560,92 660,88 L660,100 C562,104 450,122 374,192 C292,274 190,380 0,384 Z" fill="var(--green)"/>
      <path d="M0,356 C170,350 270,246 350,166 C430,96 555,76 660,72" fill="none" stroke="var(--purple)" stroke-width="4"/>
      <path d="M0,854 L0,802 C220,802 440,792 660,774 L660,854 Z" fill="var(--green-light)"/>
      <path d="M0,794 C220,794 440,784 660,766" fill="none" stroke="var(--purple)" stroke-width="5"/>
    </svg>

    <aside class="gift-badge">
      <div class="gift-art" role="img" aria-label="Wrapped gift box"></div>
      <div class="lead">Get a</div>
      <div class="amount">$50</div>
      <div class="card">Prixa Gift Card</div>
      <div class="who">for New Customers</div>
      <div class="cta">Call Today</div>
      <div class="limit">Limited time offer</div>
    </aside>

    <div class="brand">Breathwell Depot</div>

    <header class="headline">
      <h1>BETTER SLEEP FOR BETTER HEALTH</h1>
      <p class="region">Serving the Regions of Niagara and Hamilton</p>
      <p class="insurance">We accept all health insurances</p>
    </header>

    <div class="offer-pill">We Offer You So Much More</div>

    <section class="benefits">
      <div class="benefit">
        <div class="benefit-icon">
          <svg width="40" height="30" viewBox="0 0 40 30" fill="#fff"><rect x="2" y="4" width="22" height="16" rx="2"/><path d="M24 9h8l6 6v5H24z"/><circle cx="9" cy="23" r="4"/><circle cx="31" cy="23" r="4"/></svg>
        </div>
        <p class="free">FREE</p>
        <p class="label">Delivery Of Supplies</p>
      </div>
      <div class="benefit">
        <div class="benefit-icon">
          <svg width="38" height="34" viewBox="0 0 38 34" fill="#fff"><path d="M19 2 2 16h5v16h9V22h6v10h9V16h5z"/></svg>
        </div>
        <p class="free">FREE</p>
        <p class="label">Home Visits</p>
      </div>
      <div class="benefit">
        <div class="benefit-icon">
          <svg width="36" height="36" viewBox="0 0 36 36"><rect x="3" y="6" width="30" height="27" rx="3" fill="#fff"/><rect x="3" y="6" width="30" height="8" fill="#d8f2e3"/><rect x="9" y="2" width="4" height="8" rx="2" fill="#fff"/><rect x="23" y="2" width="4" height="8" rx="2" fill="#fff"/><text x="18" y="29" text-anchor="middle" font-size="13" font-weight="700" fill="#1e9e5a" font-family="Open Sans, sans-serif">25</text></svg>
        </div>
        <p class="label">Night And Weekend Appointments.</p>
      </div>
      <div class="benefit">
        <div class="benefit-icon">
          <svg width="40" height="34" viewBox="0 0 40 34" fill="#fff"><circle cx="10" cy="7" r="4"/><circle cx="30" cy="7" r="4"/><path d="M5 14h10v18H5zM25 14h10v18H25z"/><path d="M15 18h10v3H15z"/><text x="20" y="12" text-anchor="middle" font-size="10" font-weight="800" font-family="Open Sans, sans-serif">$</text></svg>
        </div>
        <p class="label">We Buy Your Old Supplies</p>
      </div>
    </section>

    <section class="actions">
      <div class="action call">
        <small>For More Information</small>
        <div class="big">Call: 289-517-3064</div>
      </div>
      <div class="action web">
        <small>Or Visit Our Website</small>
        <div class="big">www.<span class="hl">Breathwell</span>Depot-example.com</div>
      </div>
    </section>

    <p class="tagline">We Make CPAP <b>Personal</b></p>
  </main>
</body>
</html>
```